Business Card Design Project

2 sided business card utilizing existing logo
- English on one side, Arabic on the other side (both English and Arabic text will be provided)
Same color scheme as logo
Information included will be: name, title, email, phone, address and website (www.veralunix.com)
Updates

Target Market(s)

We are a Systems Integration Company

Industry/Entity Type

Business

Font styles to use
Serif
Sans Serif

Requirements
Should not have
• We prefer using the flat logo rather than one with shadow/3D effect

```html
<!DOCTYPE html>
<html lang="en">
<head>
<meta charset="utf-8">
<title>Veralunix Business Card</title>
<link rel="stylesheet" href="https://fonts.googleapis.com/css2?family=Exo+2:wght@400;500;700&display=swap">
<style>
  :root {
    --brand-red: #e3161c;
    --paper-light: #ffffff;
    --paper-shade: #d9d9d9;
    --ink-dark: #2a2a2a;
    --ink-light: #ffffff;
    --backdrop: #eceae7;
  }
  * { box-sizing: border-box; margin: 0; padding: 0; }
  html, body {
    width: 1200px;
    height: 870px;
    overflow: hidden;
    background: var(--backdrop);
    font-family: "Exo 2", sans-serif;
  }
  .stage {
    position: relative;
    width: 1200px;
    height: 870px;
    display: flex;
    align-items: center;
    justify-content: center;
    gap: 30px;
  }
  .card {
    position: relative;
    width: 560px;
    height: 320px;
    overflow: hidden;
    background: linear-gradient(160deg, var(--paper-light) 0%, #f1f1f1 45%, var(--paper-shade) 100%);
    box-shadow: 0 6px 18px rgba(0,0,0,0.18);
  }
  .brand {
    display: flex;
    align-items: center;
    gap: 8px;
    color: var(--brand-red);
    font-weight: 700;
    letter-spacing: 3px;
  }
  .brand-mark {
    display: block;
    background: var(--brand-red);
  }

  /* Front side */
  .contact-list {
    position: absolute;
    left: 38px;
    top: 24px;
    list-style: none;
  }
  .contact-list li {
    display: flex;
    align-items: center;
    gap: 9px;
    height: 21px;
    font-size: 13px;
    color: var(--ink-dark);
    letter-spacing: 0.5px;
  }
  .contact-list svg { width: 12px; height: 12px; fill: var(--brand-red); flex: none; }
  .front .brand {
    position: absolute;
    right: 38px;
    top: 128px;
    font-size: 21px;
  }
  .front .brand-mark { width: 14px; height: 14px; }
  .info-band {
    position: absolute;
    left: 0;
    right: 0;
    bottom: 0;
    height: 146px;
    background: var(--brand-red);
    color: var(--ink-light);
  }
  .address {
    position: absolute;
    left: 38px;
    top: 20px;
    font-size: 15px;
    line-height: 21px;
    letter-spacing: 0.6px;
    font-style: normal;
  }
  .holder {
    position: absolute;
    right: 38px;
    bottom: 30px;
    text-align: right;
  }
  .holder-name {
    font-size: 18px;
    font-weight: 500;
    letter-spacing: 1px;
  }
  .holder-title {
    font-size: 14px;
    letter-spacing: 0.6px;
    margin-top: 2px;
  }

  /* Back side */
  .back {
    display: flex;
    align-items: center;
    justify-content: center;
  }
  .back .brand { font-size: 34px; gap: 14px; }
  .back .brand-mark { width: 24px; height: 24px; }
</style>
</head>
<body>
<main class="stage">
  <section class="card front" aria-label="Card front">
    <ul class="contact-list">
      <li>
        <svg viewBox="0 0 12 12" aria-hidden="true"><path d="M2.5 0.8l2 2.2-1 1.3c.7 1.5 1.7 2.5 3.2 3.2l1.3-1 2.2 2-1.2 2.2C4.8 10.4 1.6 7.2.8 2z"/></svg>
        012 555 0147
      </li>
      <li>
        <svg viewBox="0 0 12 12" aria-hidden="true"><path d="M3 0h6v12H3zM4 1.5v8h4v-8z"/></svg>
        012 555 0148
      </li>
      <li>
        <svg viewBox="0 0 12 12" aria-hidden="true"><path d="M3 0h5v3H3zM1 4h10v6H9v2H3v-2H1zM4 8v3h4V8z"/></svg>
        012 555 0149
      </li>
      <li>
        <svg viewBox="0 0 12 12" aria-hidden="true"><path d="M0 2h12v1L6 7 0 3zM0 4.5l6 4 6-4V10H0z"/></svg>
        info@veralunix.com
      </li>
      <li>
        <svg viewBox="0 0 12 12" aria-hidden="true"><circle cx="6" cy="6" r="6"/></svg>
        www.veralunix.com
      </li>
    </ul>
    <div class="brand"><span class="brand-mark"></span>VERALUNIX</div>
    <div class="info-band">
      <address class="address">047,12th floor,Harbor<br>Point Road QRT</address>
      <div class="holder">
        <div class="holder-name">DANIEL MERCER</div>
        <div class="holder-title">Managing Director</div>
      </div>
    </div>
  </section>

  <section class="card back" aria-label="Card back">
    <div class="brand"><span class="brand-mark"></span>VERALUNIX</div>
  </section>
</main>
</body>
</html>
```